Flyer Design / Authenticity Certificate - Art Work

Looking for a design of a "Authenticity Certificate" - flyer, that will include some basic company info like logo etc, and allow our in house artist to sign and authenticate before it is applied the reverse of one of the paintings we will sell. Linked with our online sales website - "Amber Harbor Studios", where we recreate one off oil paintings from digital photographs. Our business logo should be incorporated in the design, along with a section for "Artisit Name" "Artisit Signature" "Ref Code"
Updates

Hi.. Sorry I should have added the size we need - please design accordingly to A6. Thanks.

Industry/Entity Type

It Company

Font styles to use
Serif
Script

Colors

Designer to choose colors to be used in the design.

Requirements
Must have
• Company logo
• Area for artist to print and sign
• Area for a reference
Nice to have
• must use the logo, maybe incorporate a "seal" icon, like what was used as a wax seal on older style documents

```html
<!DOCTYPE html>
<html lang="en">
<head>
<meta charset="utf-8">
<title>Certificate of Authenticity – Amber Harbor Studios</title>
<link href="https://fonts.googleapis.com/css2?family=Open+Sans:wght@400;600;700&display=swap" rel="stylesheet">
<style>
  :root {
    --page-bg: #e6e6e6;
    --card-bg: #ffffff;
    --ink: #333333;
    --ink-soft: #3c3c3c;
    --tone-warm: #f6c58f;
    --tone-neutral: #d4d4d4;
    --tone-cool: #9fd3ea;
    --tone-rose: #ee9aa6;
    --rule: #a3338f;
    --divider: #c9a3c2;
    --placeholder: #9a9a9a;
  }
  * { box-sizing: border-box; margin: 0; padding: 0; }
  html, body { width: 1200px; height: 982px; overflow: hidden; }
  body {
    background: var(--page-bg);
    font-family: "Open Sans", sans-serif;
    color: var(--ink);
    position: relative;
  }
  .certificate {
    position: absolute;
    left: 50px; top: 100px;
    width: 1100px; height: 781px;
    background: var(--card-bg);
    overflow: hidden;
  }
  .certificate__header-band {
    position: absolute;
    left: 0; top: 0;
    width: 1100px; height: 110px;
    background: linear-gradient(90deg, var(--tone-warm) 0%, var(--tone-neutral) 35%, var(--tone-cool) 65%, var(--tone-rose) 100%);
  }
  .certificate__title {
    position: absolute;
    left: 141px; top: 180px;
    width: 370px;
    text-align: center;
    line-height: 1;
  }
  .certificate__title-main {
    display: block;
    font-size: 54px; font-weight: 700;
  }
  .certificate__title-sub {
    display: block;
    margin-top: 10px;
    font-size: 28px; font-weight: 600;
  }
  .brand {
    position: absolute;
    left: 830px; top: 128px;
    width: 260px;
    text-align: center;
  }
  .brand__mark {
    width: 82px; height: 82px;
    margin: 0 auto 14px;
    border-radius: 50%;
    background: var(--ink);
  }
  .brand__name {
    font-size: 17px; font-weight: 600;
    letter-spacing: 1px;
    white-space: nowrap;
    color: var(--ink-soft);
    text-transform: uppercase;
  }
  .artwork-slot {
    position: absolute;
    left: 106px; top: 335px;
    width: 222px; height: 222px;
    border: 1.5px dotted var(--placeholder);
    border-radius: 50%;
    display: flex; align-items: center; justify-content: center;
  }
  .artwork-slot__plus { width: 34px; height: 34px; }
  .certificate__divider {
    position: absolute;
    left: 415px; top: 320px;
    width: 2px; height: 262px;
    background: var(--divider);
  }
  .certificate__statement {
    position: absolute;
    left: 478px; top: 314px;
    width: 587px;
    font-size: 18px; line-height: 26px;
    text-align: justify;
    color: var(--ink-soft);
  }
  .field {
    position: absolute;
    text-align: center;
    border-top: 2px dotted var(--rule);
    padding-top: 6px;
    font-size: 19px;
    color: var(--ink-soft);
    white-space: nowrap;
  }
  .field--artist-name { left: 577px; top: 542px; width: 385px; font-size: 20px; }
  .field--edition  { left: 53px;  top: 684px; width: 214px; }
  .field--title    { left: 314px; top: 684px; width: 188px; }
  .field--type     { left: 551px; top: 684px; width: 188px; }
  .field--signature{ left: 838px; top: 684px; width: 214px; }
  .certificate__contact {
    position: absolute;
    left: 0; top: 748px; width: 100%;
    text-align: center;
    font-size: 16px;
    color: var(--ink-soft);
  }
</style>
</head>
<body>
  <main class="certificate">
    <div class="certificate__header-band" role="img" aria-label="Colourful decorative header band"></div>

    <h1 class="certificate__title">
      <span class="certificate__title-main">CERTIFICATE</span>
      <span class="certificate__title-sub">Of Authenticity</span>
    </h1>

    <div class="brand">
      <div class="brand__mark"></div>
      <p class="brand__name">Amber Harbor Studios</p>
    </div>

    <div class="artwork-slot" role="img" aria-label="Space for a small image of the artwork">
      <svg class="artwork-slot__plus" viewBox="0 0 34 34" aria-hidden="true">
        <rect x="15" y="2" width="4" height="30" fill="var(--ink)"/>
        <rect x="2" y="15" width="30" height="4" fill="var(--ink)"/>
      </svg>
    </div>

    <div class="certificate__divider"></div>

    <p class="certificate__statement">This certificate of authentication certifies the identification of the artwork here beneath, and is offered in an authorised signed and numbered limited edition. No reproduction is permitted without express permission of the artist.</p>

    <div class="field field--artist-name">Name Of Artist</div>
    <div class="field field--edition">Edition No</div>
    <div class="field field--title">Title</div>
    <div class="field field--type">Type</div>
    <div class="field field--signature">Artist Signature</div>

    <p class="certificate__contact">coa@amberharborstudios.com</p>
  </main>
</body>
</html>
```